Professional PowerPoint Template for Data Reports, Presentations

We are a small leadership coaching/consulting firm and would like to update our PowerPoint template that we use with our clients, who are typically mid-senior level company professionals. I've attached a sample Powerpoint as well as our branding guide. The cover page is what needs the most work - just doesn't look current/professional enough. We do want to keep the pages after that clean, with come color but enough space for text and graphics.
Target Market(s)
Senior mgmt and HR executives in small-mid sized companies
Font styles to use
Sans Serif
Requirements
Must have
- Professional
- Clean
- Tied to company color scheme/logo
Nice to have
- Our title pages don't usually have many words on them; we'd like a design that has a lot of color - probably still using mainly our blue but accented with other colors.
- Need simple but smart looking pages after cover with lot of space; mostly we have text on the slides. Currently this is often in bullet point style, but we could probably upgrade the options there.
Should not have
- Anything that looks like a marketing style, as we typically use these with our current clients to share results of data collected, project plans, etc.

```html
<!DOCTYPE html>
<html lang="en">
<head>
<meta charset="utf-8">
<title>Halvern – Presentation Template</title>
<link rel="stylesheet" href="https://fonts.googleapis.com/css2?family=Montserrat:wght@500;600&display=swap">
<style>
  :root {
    --brand-blue: #1f4bb4;
    --navy: #0c2550;
    --coral: #ff6a48;
    --mint: #72e3a7;
    --mist: #f0f5f4;
    --white: #ffffff;
    --sea-light: #b9d8ef;
    --sea-mid: #3f7cc8;
    --sea-deep: #030a17;
  }
  * { box-sizing: border-box; margin: 0; padding: 0; }
  html, body { width: 1200px; height: 907px; overflow: hidden; background: var(--white); }
  body { position: relative; font-family: "Montserrat", sans-serif; }

  .slide { position: absolute; overflow: hidden; }

  /* Cover slide */
  .cover { left: 0; top: 0; width: 591px; height: 443px; background: var(--white); }
  .cover__photo { position: absolute; top: 0; height: 443px; }
  .cover__photo--left  { left: 0; width: 188px;
    background: linear-gradient(180deg, #cfe3f3 0%, #9fc6e6 22%, #3d75c0 45%, #123f86 72%, var(--sea-deep) 100%); }
  .cover__photo--centre { left: 192px; width: 208px;
    background: linear-gradient(180deg, #d6e8f6 0%, var(--sea-light) 25%, #7aa6d6 45%, #4a6fa6 62%, #2f3b57 78%, #2d3a55 100%); }
  .cover__photo--right { left: 404px; width: 187px;
    background: linear-gradient(180deg, #6ea8dc 0%, #4f92d6 25%, var(--sea-mid) 38%, #15408c 58%, #061633 78%, var(--sea-deep) 100%); }
  .cover__name { position: absolute; left: 206px; top: 205px; width: 180px;
    display: flex; align-items: center; gap: 9px;
    color: var(--white); font-weight: 500; font-size: 25px; letter-spacing: 3px; }
  .cover__dot { width: 26px; height: 26px; border: 2px solid var(--white); border-radius: 50%; flex: none; }

  /* Brand tab on content slides */
  .brand-tab { position: absolute; width: 37px; height: 111px; top: 46px; right: 5px;
    display: flex; flex-direction: column; align-items: center; justify-content: flex-start;
    padding-top: 8px; gap: 7px; color: var(--white); }
  .brand-tab__mark { width: 9px; height: 9px; border: 1.5px solid var(--white); border-radius: 50%; }
  .brand-tab__name { writing-mode: vertical-rl; transform: rotate(180deg);
    font-weight: 600; font-size: 10.5px; letter-spacing: 1.2px; }

  /* Section slide (blue) */
  .section { left: 608px; top: 0; width: 592px; height: 443px; background: var(--brand-blue); }
  .section__edge { position: absolute; right: 0; top: 0; width: 5px; height: 100%; background: var(--coral); }
  .section__frame { position: absolute; left: 252px; top: 46px; width: 275px; height: 351px; border: 3px solid var(--white); }
  .section__rule { position: absolute; left: 296px; width: 178px; height: 2px; background: var(--white); }
  .section__rule--top { top: 157px; }
  .section__rule--bottom { top: 288px; }
  .section .brand-tab { background: var(--coral); }

  /* Content slide (light) */
  .content { left: 0; top: 463px; width: 586px; height: 444px; background: var(--mist); }
  .content__band { position: absolute; left: 0; top: 0; width: 37px; height: 100%; background: var(--coral); }
  .content__edge { position: absolute; right: 0; top: 0; width: 4px; height: 100%; background: var(--brand-blue); }
  .content__frame { position: absolute; left: 95px; top: 47px; width: 434px; height: 351px; border: 8px solid var(--white); }
  .content__connector { position: absolute; left: 529px; top: 220px; width: 53px; height: 3px; background: var(--white); }
  .content .brand-tab { right: 4px; top: 47px; background: var(--brand-blue); }

  /* Content slide (mint) */
  .feature { left: 608px; top: 463px; width: 592px; height: 444px; background: var(--mist); }
  .feature__block { position: absolute; left: 186px; top: 0; width: 401px; height: 100%; background: var(--mint); }
  .feature__notch { position: absolute; left: 186px; top: 63px; width: 100px; height: 318px; background: var(--mist); }
  .feature__edge { position: absolute; right: 0; top: 0; width: 5px; height: 100%; background: var(--navy); }
  .feature .brand-tab { top: 47px; background: var(--navy); }
</style>
</head>
<body>

  <section class="slide cover">
    <div class="cover__photo cover__photo--left" role="img" aria-label="Calm sea under a hazy sky, left panel"></div>
    <div class="cover__photo cover__photo--centre" role="img" aria-label="Calm sea with distant mountains, centre panel"></div>
    <div class="cover__photo cover__photo--right" role="img" aria-label="Deep blue sea fading to dark water, right panel"></div>
    <div class="cover__name"><span class="cover__dot"></span><span>HALVERN</span></div>
  </section>

  <section class="slide section">
    <div class="section__frame"></div>
    <div class="section__rule section__rule--top"></div>
    <div class="section__rule section__rule--bottom"></div>
    <div class="section__edge"></div>
    <div class="brand-tab"><span class="brand-tab__mark"></span><span class="brand-tab__name">HALVERN</span></div>
  </section>

  <section class="slide content">
    <div class="content__band"></div>
    <div class="content__frame"></div>
    <div class="content__connector"></div>
    <div class="content__edge"></div>
    <div class="brand-tab"><span class="brand-tab__mark"></span><span class="brand-tab__name">HALVERN</span></div>
  </section>

  <section class="slide feature">
    <div class="feature__block"></div>
    <div class="feature__notch"></div>
    <div class="feature__edge"></div>
    <div class="brand-tab"><span class="brand-tab__mark"></span><span class="brand-tab__name">HALVERN</span></div>
  </section>

</body>
</html>
```